Cafe menu flyer design

I need if possible A4 double sided menus. Two exemplars: first will contain breakfast menu on one side & refreshments menu on the other side, second exemplar will contain lunch menu on one side & refreshments menu on the other side. We do not need a description of the cafe or any history on these flyers, but design should reflect our surroundings and activities this area. We are located in main ski resort in UK-Cairngorm Mountains, right on the main ski road. The slopes are only 2 miles away from us. We are also very popular with wild life enthusiasts. Continues in design brief!

```html
<!DOCTYPE html>
<html lang="en">
<head>
<meta charset="utf-8">
<title>Cafe Menu Flyers</title>
<link rel="stylesheet" href="https://fonts.googleapis.com/css2?family=Marcellus&family=Crimson+Pro:wght@400;600&display=swap">
<style>
:root{
  --page-bg:#e9e4da;
  --paper-light:#e2d4ad;
  --paper-mid:#d5c393;
  --paper-edge:#b99a62;
  --band:#4b3c24;
  --band-dark:#3a2e1b;
  --gold:#c9b260;
  --gold-line:#b8993f;
  --ink:#3a2e1e;
  --title-ink:#4a3820;
  --photo-snow-top:#9fb6d2;
  --photo-snow-bottom:#dde4ec;
  --photo-jacket-top:#b9d8e0;
  --photo-jacket-bottom:#e4eaef;
}
*{margin:0;padding:0;box-sizing:border-box}
html,body{width:1200px;height:1000px;overflow:hidden;background:var(--page-bg)}
.canvas{position:relative;width:1200px;height:1000px}
.sheet{
  position:absolute;top:125px;width:546px;height:773px;
  background:radial-gradient(ellipse at 50% 45%,var(--paper-light) 0%,var(--paper-mid) 65%,var(--paper-edge) 100%);
  font-family:"Crimson Pro",Georgia,serif;color:var(--ink);
  box-shadow:0 2px 6px rgba(0,0,0,.25);
}
.sheet--breakfast{left:47px}
.sheet--refreshments{left:620px}
.header-band{
  position:absolute;left:0;top:25px;width:100%;height:90px;
  background:linear-gradient(var(--band),var(--band-dark));
}
.cafe-name{
  position:absolute;left:0;right:0;top:34px;text-align:center;
  font-family:"Marcellus",Georgia,serif;font-size:39.5px;color:var(--gold);letter-spacing:.5px;
}
.menu-title{
  position:absolute;left:0;right:0;top:120px;text-align:center;
  font-family:"Crimson Pro",Georgia,serif;font-weight:600;font-size:33px;color:var(--title-ink);
}
.menu-list{position:absolute;list-style:none;font-size:12.8px;line-height:15.4px}
.sheet--breakfast .menu-list{left:40px;right:46px;top:171px}
.sheet--refreshments .menu-list{left:39px;right:47px;top:164px}
.menu-list li{display:flex;justify-content:space-between;align-items:baseline;height:15.4px;white-space:nowrap}
.menu-list li.gap{height:15.4px}
.menu-list li .note{font-size:7px}
.menu-list li.caps{text-transform:uppercase;letter-spacing:.1px}
.price{font-weight:600}
.closing{position:absolute;font-size:12.8px;line-height:15.4px}
.sheet--breakfast .closing{left:40px;top:525px}
.sheet--refreshments .closing{left:39px;top:533px}
.rule{position:absolute;left:0;width:100%;height:2px;background:var(--gold-line)}
.rule--top{top:573px}
.rule--bottom{top:625px;height:3px}
.footer{position:absolute;left:0;right:0;top:585px;text-align:center;font-size:12.8px;line-height:15.4px}
.photo{position:absolute;left:0;top:632px;width:100%;height:141px}
.photo--skier{background:linear-gradient(180deg,var(--photo-snow-top),var(--photo-snow-bottom))}
.photo--skiers-close{background:linear-gradient(180deg,var(--photo-jacket-top),var(--photo-jacket-bottom))}
</style>
</head>
<body>
<div class="canvas">

  <section class="sheet sheet--breakfast">
    <header class="header-band">
      <div class="cafe-name">Fiona's @ Birchwood Cafe</div>
    </header>
    <h1 class="menu-title">Breakfast 9am - 12noon</h1>
    <ul class="menu-list">
      <li><span>Small breakfast</span></li>
      <li><span>(bacon, egg, sausage)</span><span class="price">£5.50</span></li>
      <li><span>Large brteakfast</span></li>
      <li><span>( bacon, egg, sausage, black pudding, potato scone, beans, tomato)</span><span class="price">£7.95</span></li>
      <li class="gap"></li>
      <li class="caps"><span>Both breakfast include tea/coffe/plain hot chocolate &amp; one</span></li>
      <li class="caps"><span>slice of toast. One free refill drink.</span></li>
      <li class="gap"></li>
      <li><span>Pancake breakfast.</span></li>
      <li><span>Three pancakes served with hot forest berry sauce and maple syrup</span><span class="price">£4.95</span></li>
      <li><span>Add three rushers of bacon</span><span class="price">£6.95</span></li>
      <li><span>Round of toast,served with butter and jam</span><span class="price">£2.00</span></li>
      <li><span>Beans on toast</span><span class="price">£3.50</span></li>
      <li><span>Beans &amp; egg on toast</span><span class="price">£4.00</span></li>
      <li><span>Beans &amp; bacon on toast</span><span class="price">£4.50</span></li>
      <li><span>Bacon roll</span><span class="price">£2.90</span></li>
      <li><span>Lorne roll</span><span class="price">£2.50</span></li>
      <li><span>Black pudding roll</span><span class="price">£2.50</span></li>
      <li><span>Fried egg roll</span><span class="price">£2.00</span></li>
      <li><span>2 item roll</span><span class="price">£4.00</span></li>
      <li><span>Rolls with assorted cold fillings</span><span class="price">£2.20 - £3.20</span></li>
      <li><span>Pies assorted</span><span class="price">£2.50</span></li>
    </ul>
    <p class="closing">Gluten free bread, cakes and veggie breakfast available- ask staff!<br>At the hight of the season evening meals vailable. Ask staff for more information.</p>
    <div class="rule rule--top"></div>
    <footer class="footer">Birchwood, Kinraven, PH40 2XY. Tel:01234567890<br>Like us on our social page</footer>
    <div class="rule rule--bottom"></div>
    <div class="photo photo--skier" role="img" aria-label="Photo of a skier on a snowy slope with a mountain range behind"></div>
  </section>

  <section class="sheet sheet--refreshments">
    <header class="header-band">
      <div class="cafe-name">Fiona's @ Birchwood Cafe</div>
    </header>
    <h1 class="menu-title">Refreshments</h1>
    <ul class="menu-list">
      <li><span>Filter Coffee, decaf coffee, plain hot chocolate</span><span class="price">£2.00</span></li>
      <li><span>Selection of herbal teas</span><span class="price">£2.00</span></li>
      <li><span>Specialty strawberry, raspberry, apple &amp; mint tea</span></li>
      <li><span class="note">(black tea with your choice of syrup)</span><span class="price">£2.50</span></li>
      <li><span>Assorted premium “Leaf House” teas</span><span class="price">£2.50</span></li>
      <li><span>Hot chocolate with cream</span><span class="price">£2.20</span></li>
      <li><span>Hot chocolate with marsh mallows</span><span class="price">£2.20</span></li>
      <li><span>Hot chocolate with cream &amp; marsh mallows</span><span class="price">£2.20</span></li>
      <li><span>Hot chocolate with brandy</span><span class="price">£3.50</span></li>
      <li><span>Hot chocolate with brandy, marsh mallows &amp; cream</span><span class="price">£4.50</span></li>
      <li><span>Cafe Latte/Cappucino</span><span class="price">£2.50</span></li>
      <li><span>Squirrel Latte</span><span class="price">£3.50</span></li>
      <li><span>Chocolate Latte</span><span class="price">£3.50</span></li>
      <li><span>Cinnamon Latte</span><span class="price">£3.50</span></li>
      <li><span>Caramel Latte</span><span class="price">£3.50</span></li>
      <li><span>Butterscotch Latte</span><span class="price">£3.50</span></li>
      <li><span>Gingerbread Latte</span><span class="price">£3.50</span></li>
      <li><span>Mocha</span><span class="price">£3.50</span></li>
      <li><span>Glass of milk</span><span class="price">£1.20</span></li>
      <li><span>Milkshakes</span><span class="price">£2.00</span></li>
      <li><span>Still or Sparkling water</span><span class="price">£1.80</span></li>
      <li><span>Cans of juice</span><span class="price">£1.60</span></li>
      <li><span>Cartons of juice</span><span class="price">£1.30</span></li>
    </ul>
    <p class="closing">We use semi skimmed milk only<br>At the hight of the season evening meals vailable. Ask staff for more information.</p>
    <div class="rule rule--top"></div>
    <footer class="footer">Birchwood, Kinraven, PH40 2XY. Tel:01234567890<br>Like us on our social page</footer>
    <div class="rule rule--bottom"></div>
    <div class="photo photo--skiers-close" role="img" aria-label="Close-up photo of skiers in winter jackets and gloves among snowy trees"></div>
  </section>

</div>
</body>
</html>
```